Zuvto..Hydrating sports energy drink

"Zuvto" is a hydrating, all-natural energy beverage geared towards health focused consumers and athletes
While other energy drinks are carbonated and artificially flavored, Zuvto's
light and refreshing all-natural formula tastes more like a sports drink without the heavy after effects
Zuvto's tropical, vitamin rich taste provides the hydration and burst of energy to help you perform at your best with out the calories....

Target Market(s)

hispanic males teen to 24 yrs old -with a cross over to the 18-35 yr old female due to it all-natural formula low in calories no sugar
this is a logo and bottle package design request. We have left it open to the arist vision
on how will look.

Thank you..Good luck!!!

Industry/Entity Type

Health

Requirements
Nice to have
• contrasting image ,

Several ideas have been submitted which look pretty good .

I like to have a contrasting design done as follows :

Think of a Spartan warrior caricature holding a shield in one hand , on the shield is our brand name Zuveto
.. in the other hand he is holding a lighting bolt he is standing on a bluff over looking a clear refreshing looking lake

```html
<!DOCTYPE html>
<html lang="en">
<head>
<meta charset="utf-8">
<title>Zuvto Natural Energy – Can Label</title>
<link rel="stylesheet" href="https://fonts.googleapis.com/css2?family=Jost:wght@400;500;600;700;800&family=Arimo:wght@400;700&display=swap">
<style>
  :root {
    --lime: #8ef700;
    --lime-deep: #6fd400;
    --night: #1b1238;
    --violet: #2d1b5e;
    --violet-mid: #3a2474;
    --panel: #1a1236;
    --ink: #1e1244;
    --white: #ffffff;
  }
  * { margin: 0; padding: 0; box-sizing: border-box; }
  html, body { width: 1200px; height: 652px; overflow: hidden; background: var(--night); }
  .label {
    position: relative; width: 1200px; height: 652px; overflow: hidden;
    font-family: "Jost", sans-serif; color: var(--white);
  }
  .droplet-field {
    position: absolute; left: 0; top: 20px; width: 1200px; height: 620px;
    background: radial-gradient(ellipse at 55% 45%, var(--violet-mid) 0%, var(--violet) 45%, var(--night) 100%);
  }
  .top-band { position: absolute; left: 0; top: 0; }
  .bottom-band { position: absolute; left: 0; top: 575px; width: 1200px; height: 23px; background: var(--lime); }
  .headline { position: absolute; left: 580px; top: 52px; width: 212px; color: var(--ink); text-align: center; }
  .headline-small { font-weight: 700; font-size: 27px; letter-spacing: 12px; line-height: 30px; margin-right: -12px; }
  .headline-big { font-weight: 800; font-size: 53px; line-height: 50px; letter-spacing: 0; }

  .divider { position: absolute; left: 380px; top: 20px; }
  .brand-vertical {
    position: absolute; left: 470px; top: 365px; transform: translate(-50%, -50%) rotate(-90deg);
    font-weight: 800; font-size: 160px; line-height: 1; color: var(--lime); white-space: nowrap; letter-spacing: -2px;
  }

  .nutrition { position: absolute; left: 60px; top: 210px; width: 181px; font-family: "Arimo", sans-serif; color: var(--white); }
  .nutrition-title {
    background: var(--lime); color: var(--ink); font-weight: 700; font-size: 11px;
    text-align: center; height: 22px; line-height: 22px; border-radius: 9px 9px 0 0;
  }
  .nutrition-body { border: 1px solid var(--white); border-top: none; font-size: 7px; }
  .nutrition-body .row { padding: 2px 4px; line-height: 10px; }
  .nutrition-body .rule { border-top: 1px solid var(--white); }
  .nutrition-body .thick { border-top: 4px solid var(--white); }
  .facts { width: 100%; border-collapse: collapse; font-size: 6.6px; }
  .facts th { font-weight: 400; text-align: center; line-height: 8px; padding: 2px 1px; border-left: 1px solid var(--white); }
  .facts th:first-child { border-left: none; }
  .facts td { line-height: 10.6px; padding: 0 3px; border-left: 1px solid var(--white); text-align: center; }
  .facts td:first-child { border-left: none; text-align: left; }
  .facts thead tr { border-bottom: 1px solid var(--white); }
  .facts .spacer td { height: 12px; }
  .pair { display: flex; justify-content: space-between; }

  .panel { position: absolute; left: 628px; top: 188px; }
  .panel-content { position: absolute; left: 645px; width: 140px; }
  .brand-mark { top: 238px; left: 684px; width: 96px; height: 96px; border: 2px solid #4a2ca0; border-radius: 50%; position: absolute; }
  .brand-name { position: absolute; left: 640px; top: 342px; width: 148px; text-align: center; font-size: 15px; letter-spacing: 3px; font-weight: 400; }
  .reg { position: absolute; left: 766px; top: 243px; font-size: 8px; }
  .tagline { top: 408px; color: var(--lime); font-weight: 700; font-size: 14.5px; line-height: 17px; text-align: center; left: 640px; width: 148px; }
  .blurb { top: 481px; font-size: 11px; line-height: 12.5px; font-weight: 500; left: 651px; width: 132px; }
  .volume { top: 544px; font-size: 15px; font-weight: 700; left: 640px; width: 148px; text-align: center; }

  .recycle { position: absolute; left: 1080px; top: 480px; width: 60px; height: 60px; border-radius: 50%; border: 5px solid var(--white); }
</style>
</head>
<body>
<main class="label">
  <div class="droplet-field" role="img" aria-label="Water droplet texture on a deep purple can surface"></div>

  <svg class="top-band" width="1200" height="190" viewBox="0 0 1200 190" aria-hidden="true">
    <rect x="0" y="0" width="1200" height="20" fill="#241646"/>
    <path d="M0 20 H1200 V172 C1050 150 880 125 680 132 C520 138 430 150 300 170 C200 180 90 178 0 172 Z" fill="var(--lime)"/>
    <path d="M300 170 C430 150 520 138 680 132 C880 125 1050 150 1200 172 V176 C1050 156 880 131 680 138 C520 144 430 156 300 176 Z" fill="var(--lime-deep)" opacity="0.5"/>
  </svg>

  <div class="headline">
    <div class="headline-small">NATURAL</div>
    <div class="headline-big">ENERGY</div>
  </div>

  <svg class="divider" width="6" height="560" viewBox="0 0 6 560" aria-hidden="true">
    <line x1="3" y1="0" x2="3" y2="555" stroke="var(--ink)" stroke-width="5"/>
  </svg>

  <div class="brand-vertical">Zuvto</div>

  <section class="nutrition">
    <div class="nutrition-title">Nutritional Information</div>
    <div class="nutrition-body">
      <div class="row">Servings per package: 2</div>
      <div class="row">Serving size: 250 ml</div>
      <div class="row thick">Amount Per Serving</div>
      <div class="row rule pair"><span>Calories 40</span><span style="margin-right:30px">Calories from Fat 0</span></div>
      <table class="facts" style="border-top:1px solid #fff">
        <thead>
          <tr><th style="width:58px"></th><th>Quantity<br>per serving</th><th>Quantity<br>per 100ml</th><th>% daily<br>value</th></tr>
        </thead>
        <tbody>
          <tr><td>Energy (KJ)</td><td>167 mg</td><td>70 mg</td><td></td></tr>
          <tr><td>(Kcal)</td><td>40 mg</td><td>17 mg</td><td></td></tr>
          <tr><td>Protein</td><td>0 g</td><td>0 g</td><td></td></tr>
          <tr><td>Fat</td><td>0 g</td><td>0 g</td><td>0%</td></tr>
          <tr><td>Saturated Fat</td><td>0 g</td><td>0 g</td><td>0%</td></tr>
          <tr><td>Trans Fat</td><td>0 g</td><td>0 g</td><td>0%</td></tr>
          <tr><td>Cholesterol</td><td>0 mg</td><td>0 g</td><td>0%</td></tr>
          <tr><td>Sodium</td><td>44 mg</td><td>18 mg</td><td>2%</td></tr>
          <tr><td>Carbohydrates</td><td>10 g</td><td>42 mg</td><td>3%</td></tr>
          <tr><td>Dietary Fiber</td><td>0 g</td><td>0 g</td><td>0%</td></tr>
          <tr><td>Sugars</td><td>9.6 g</td><td>4.0 g</td><td></td></tr>
          <tr><td>Protein</td><td>0 g</td><td>0 g</td><td></td></tr>
          <tr><td>Potassium</td><td>482 mg</td><td>201 mg</td><td></td></tr>
          <tr class="spacer"><td></td><td></td><td></td><td></td></tr>
        </tbody>
      </table>
      <div class="row thick pair"><span>Vitamin A &nbsp;&nbsp;0%</span><span>Vitamin C &nbsp;&nbsp;0%</span></div>
      <div class="row rule pair"><span>Calcium &nbsp;&nbsp;&nbsp;&nbsp;4%</span><span style="margin-right:18px">Iron &nbsp;&nbsp;4%</span></div>
      <div class="row rule">Percent Daily intake based on a 2,000 calorie diet</div>
      <div class="row rule">Ingredient: Distilled Water</div>
    </div>
  </section>

  <svg class="panel" width="162" height="386" viewBox="0 0 162 386" aria-hidden="true">
    <path d="M0 0 H160 V386 H0 V290 C35 250 38 180 22 120 C14 80 10 40 0 20 Z" fill="var(--panel)"/>
    <path d="M0 20 C10 40 14 80 22 120 C38 180 35 250 0 290 Z" fill="#3c2480"/>
  </svg>
  <div class="brand-mark" aria-hidden="true"></div>
  <div class="reg">®</div>
  <div class="brand-name">ZUVTO</div>
  <div class="panel-content tagline" style="position:absolute">PURA ENERGIA<br>&amp; VITALIDAD</div>
  <p class="panel-content blurb" style="position:absolute">Zuvto natural energy drink is packed with vatimins to keep you hydrated.</p>
  <div class="panel-content volume" style="position:absolute">13oz</div>

  <div class="recycle" aria-hidden="true"></div>

  <div class="bottom-band"></div>
</main>
</body>
</html>
```